Pagebook Ads for HOA Law Firm

We need to create certain ads for a Pagebook ads campaign. We are a law firm in Florida that represents homeowners against HOAs. We need to create the following ads:

1. Image Ads Specifications:

File Type: JPG or PNG
Ratio: 1.91:1 to 4:5
Resolution:
a) 1:1 ratio: 1080 x 1080 pixels
b) 4:5 ratio: 1080 x 1350 pixels
Maximum File Size: 30MB
Minimum Width: 600 pixels
Minimum Height:
a) 1:1 ratio: 600 pixels
b) 4:5 ratio: 750 pixels
Key Elements to Include in the Ads:

1) Headline: "HOA Violating Your Rights?"
2) Main Message: "We sue HOAs for Homeowners."
3) Firm Name: Lindqvist Harrow, P.A.
4) Website: www.covenantshieldcounsel.example
5) Phone Number: 1-800-555-0148
6) Florida Bar Compliance Statement: "Serving Homeowners in Florida with our main office in Miami-Dade."
7) Call-to-Action (CTA): Include a strong CTA such as “Contact us today for a consultation!”
8) Tone and Style: Professional yet approachable. The ad should emphasize trust, expertise, and our dedication to homeowners' rights.
9) Branding: Please use our firm's brand colors and fonts. Ensure that our logo is prominently placed within the ad.
10) Image Suggestions: Consider using images of Florida homes, frustrated homeowners, or visuals that evoke trust, protection, and legal authority.

```html
<!DOCTYPE html>
<html lang="en">
<head>
<meta charset="utf-8">
<title>Pagebook Ads for HOA Law Firm</title>
<link href="https://fonts.googleapis.com/css2?family=Montserrat:wght@400;700;800&family=Oswald:wght@500&display=swap" rel="stylesheet">
<style>
  :root {
    --board: #4d4d4d;
    --board-text: #d4d4d4;
    --ink-blue: #13139a;
    --brand-blue: #14148f;
    --dark-band: #1b1b1b;
    --white: #ffffff;
    --body-ink: #1a1a1a;
    --dot: #d9d9d9;
    --ring-grey: #a9a9c4;
  }
  * { margin: 0; padding: 0; box-sizing: border-box; }
  html, body { width: 1200px; height: 668px; overflow: hidden; background: var(--board); }
  .board { position: relative; width: 1200px; height: 668px; font-family: "Montserrat", sans-serif; }
  .board-title { position: absolute; left: 45px; top: 28px; color: var(--board-text); line-height: 1.05; }
  .board-title .kicker { font-size: 24px; font-weight: 400; letter-spacing: 0.5px; }
  .board-title .name { font-size: 25px; font-weight: 700; }
  .size-label { position: absolute; top: 112px; color: var(--board-text); font-size: 14px; font-weight: 400; }
  .ad { position: absolute; top: 149px; display: block; }
  .ad-square { left: 45px; }
  .ad-portrait { left: 468px; }
  .ad-compact { left: 887px; }
  .headline { font-family: "Montserrat", sans-serif; font-weight: 800; fill: var(--ink-blue); }
  .subhead { font-family: "Montserrat", sans-serif; font-weight: 700; fill: var(--body-ink); }
  .compliance { font-family: "Montserrat", sans-serif; font-weight: 400; fill: var(--white); }
  .cta-label { font-family: "Oswald", sans-serif; font-weight: 500; fill: var(--white); }
  .contact { font-family: "Montserrat", sans-serif; font-weight: 400; fill: var(--white); }
  .firm-name { font-family: "Montserrat", sans-serif; font-weight: 700; fill: var(--white); }
  .dot { fill: var(--dot); }
</style>
</head>
<body>
<div class="board">
  <div class="board-title">
    <div class="kicker">Pagebook Ads for</div>
    <div class="name">HOA Law Firm</div>
  </div>
  <div class="size-label" style="left:45px">1080x 1080</div>
  <div class="size-label" style="left:468px">1080x1350</div>
  <div class="size-label" style="left:887px">700-x-938</div>

  <svg width="0" height="0" style="position:absolute">
    <defs>
      <linearGradient id="homeScene" x1="0" y1="0" x2="0" y2="1">
        <stop offset="0" stop-color="#6fb3e8"/>
        <stop offset="0.45" stop-color="#d9dde2"/>
        <stop offset="0.75" stop-color="#7a9a5a"/>
        <stop offset="1" stop-color="#c9b9a0"/>
      </linearGradient>
      <linearGradient id="attorneys" x1="0" y1="0" x2="1" y2="0">
        <stop offset="0" stop-color="#2a3a66"/>
        <stop offset="0.5" stop-color="#3b4a72"/>
        <stop offset="1" stop-color="#7a7d84"/>
      </linearGradient>
    </defs>
  </svg>

  <!-- 1080 x 1080 -->
  <svg class="ad ad-square" width="387" height="387" viewBox="0 0 831 830">
    <rect width="831" height="830" fill="var(--white)"/>
    <circle cx="820" cy="170" r="335" fill="var(--brand-blue)"/>
    <circle cx="830" cy="160" r="320" fill="url(#homeScene)" role="img" aria-label="Photo of a white two-storey Florida home with palm trees"/>
    <path d="M0,400 C110,372 240,382 335,450 L430,830 L0,830 Z" fill="var(--dark-band)"/>
    <rect x="368" y="540" width="440" height="290" fill="url(#attorneys)" role="img" aria-label="Photo of the firm's two attorneys in suits"/>
    <circle cx="528" cy="418" r="222" fill="var(--dark-band)"/>
    <circle cx="514" cy="408" r="208" fill="var(--white)"/>
    <circle cx="512" cy="412" r="196" fill="var(--ring-grey)"/>
    <circle cx="505" cy="405" r="187" fill="var(--brand-blue)"/>
    <text class="firm-name" x="505" y="446" font-size="25" text-anchor="middle">Lindqvist Harrow, P.A.</text>
    <text class="headline" font-size="54"><tspan x="50" y="107">HOA</tspan><tspan x="50" y="162">Violating</tspan><tspan x="50" y="217">Your Rights?</tspan></text>
    <text class="subhead" font-size="29"><tspan x="57" y="282">We sue HOAs for</tspan><tspan x="57" y="315">Homeowners.</tspan></text>
    <g class="dots">
      <circle class="dot" cx="78" cy="345" r="2.5"/><circle class="dot" cx="98" cy="345" r="2.5"/><circle class="dot" cx="118" cy="345" r="2.5"/><circle class="dot" cx="138" cy="345" r="2.5"/><circle class="dot" cx="158" cy="345" r="2.5"/><circle class="dot" cx="178" cy="345" r="2.5"/><circle class="dot" cx="198" cy="345" r="2.5"/><circle class="dot" cx="218" cy="345" r="2.5"/>
      <circle class="dot" cx="78" cy="365" r="2.5"/><circle class="dot" cx="98" cy="365" r="2.5"/><circle class="dot" cx="118" cy="365" r="2.5"/><circle class="dot" cx="138" cy="365" r="2.5"/><circle class="dot" cx="158" cy="365" r="2.5"/><circle class="dot" cx="178" cy="365" r="2.5"/><circle class="dot" cx="198" cy="365" r="2.5"/><circle class="dot" cx="218" cy="365" r="2.5"/>
    </g>
    <text class="compliance" font-size="27"><tspan x="56" y="463">Serving</tspan><tspan x="56" y="495">Homeowners</tspan><tspan x="56" y="527">in Florida with</tspan><tspan x="56" y="559">our main office in</tspan><tspan x="56" y="590">Miami-Dade.</tspan></text>
    <rect x="55" y="623" width="303" height="56" rx="28" fill="var(--brand-blue)" stroke="var(--white)" stroke-width="2"/>
    <text class="cta-label" x="206" y="659" font-size="20" text-anchor="middle">Contact us today for a consultation!</text>
    <path d="M57,743 l4,-1 3,5 -2,2 c1,3 3,5 6,6 l2,-2 5,3 -1,4 c-9,0 -17,-8 -17,-17z" fill="var(--white)"/>
    <text class="contact" x="77" y="757" font-size="18">1-800-555-0148</text>
    <path d="M58,777 l12,5 -5,2 4,5 -2,2 -4,-5 -2,5z" fill="var(--white)"/>
    <text class="contact" x="77" y="790" font-size="18">www.covenantshieldcounsel.example</text>
  </svg>

  <!-- 1080 x 1350 -->
  <svg class="ad ad-portrait" width="387" height="484" viewBox="0 0 831 1038">
    <rect width="831" height="1038" fill="var(--white)"/>
    <circle cx="830" cy="195" r="385" fill="var(--brand-blue)"/>
    <circle cx="840" cy="185" r="370" fill="url(#homeScene)" role="img" aria-label="Photo of a white two-storey Florida home with palm trees"/>
    <path d="M0,555 C120,520 250,530 340,600 L430,1038 L0,1038 Z" fill="var(--dark-band)"/>
    <rect x="365" y="740" width="445" height="298" fill="url(#attorneys)" role="img" aria-label="Photo of the firm's two attorneys in suits"/>
    <circle cx="530" cy="522" r="222" fill="var(--dark-band)"/>
    <circle cx="517" cy="512" r="208" fill="var(--white)"/>
    <circle cx="515" cy="516" r="196" fill="var(--ring-grey)"/>
    <circle cx="510" cy="510" r="187" fill="var(--brand-blue)"/>
    <text class="firm-name" x="510" y="546" font-size="25" text-anchor="middle">Lindqvist Harrow, P.A.</text>
    <text class="headline" font-size="54"><tspan x="46" y="129">HOA</tspan><tspan x="46" y="185">Violating</tspan><tspan x="46" y="241">Your</tspan><tspan x="46" y="297">Rights?</tspan></text>
    <text class="subhead" font-size="29"><tspan x="54" y="375">We sue HOAs for</tspan><tspan x="54" y="408">Homeowners.</tspan></text>
    <g class="dots">
      <circle class="dot" cx="73" cy="474" r="2.5"/><circle class="dot" cx="93" cy="474" r="2.5"/><circle class="dot" cx="113" cy="474" r="2.5"/><circle class="dot" cx="133" cy="474" r="2.5"/><circle class="dot" cx="153" cy="474" r="2.5"/><circle class="dot" cx="173" cy="474" r="2.5"/><circle class="dot" cx="193" cy="474" r="2.5"/><circle class="dot" cx="213" cy="474" r="2.5"/>
      <circle class="dot" cx="73" cy="494" r="2.5"/><circle class="dot" cx="93" cy="494" r="2.5"/><circle class="dot" cx="113" cy="494" r="2.5"/><circle class="dot" cx="133" cy="494" r="2.5"/><circle class="dot" cx="153" cy="494" r="2.5"/><circle class="dot" cx="173" cy="494" r="2.5"/><circle class="dot" cx="193" cy="494" r="2.5"/><circle class="dot" cx="213" cy="494" r="2.5"/>
    </g>
    <text class="compliance" font-size="27"><tspan x="53" y="624">Serving</tspan><tspan x="53" y="656">Homeowners</tspan><tspan x="53" y="688">in Florida with</tspan><tspan x="53" y="720">our main office in</tspan><tspan x="53" y="751">Miami-Dade.</tspan></text>
    <rect x="52" y="807" width="303" height="57" rx="28" fill="var(--brand-blue)" stroke="var(--white)" stroke-width="2"/>
    <text class="cta-label" x="203" y="843" font-size="20" text-anchor="middle">Contact us today for a consultation!</text>
    <path d="M54,942 l4,-1 3,5 -2,2 c1,3 3,5 6,6 l2,-2 5,3 -1,4 c-9,0 -17,-8 -17,-17z" fill="var(--white)"/>
    <text class="contact" x="74" y="956" font-size="18">1-800-555-0148</text>
    <path d="M55,976 l12,5 -5,2 4,5 -2,2 -4,-5 -2,5z" fill="var(--white)"/>
    <text class="contact" x="74" y="989" font-size="18">www.covenantshieldcounsel.example</text>
  </svg>

  <!-- 700 x 938 -->
  <svg class="ad ad-compact" width="269" height="336" viewBox="0 0 577 721">
    <rect width="577" height="721" fill="var(--white)"/>
    <circle cx="560" cy="140" r="275" fill="var(--brand-blue)"/>
    <circle cx="568" cy="132" r="263" fill="url(#homeScene)" role="img" aria-label="Photo of a white two-storey Florida home with palm trees"/>
    <path d="M0,385 C90,362 180,368 245,415 L300,721 L0,721 Z" fill="var(--dark-band)"/>
    <rect x="250" y="510" width="312" height="211" fill="url(#attorneys)" role="img" aria-label="Photo of the firm's two attorneys in suits"/>
    <circle cx="372" cy="360" r="155" fill="var(--dark-band)"/>
    <circle cx="362" cy="353" r="146" fill="var(--white)"/>
    <circle cx="360" cy="356" r="137" fill="var(--ring-grey)"/>
    <circle cx="355" cy="351" r="130" fill="var(--brand-blue)"/>
    <text class="firm-name" x="355" y="378" font-size="17" text-anchor="middle">Lindqvist Harrow, P.A.</text>
    <text class="headline" font-size="38"><tspan x="33" y="88">HOA</tspan><tspan x="33" y="127">Violating</tspan><tspan x="33" y="166">Your</tspan><tspan x="33" y="205">Rights?</tspan></text>
    <text class="subhead" font-size="20"><tspan x="38" y="261">We sue HOAs for</tspan><tspan x="38" y="284">Homeowners.</tspan></text>
    <g class="dots">
      <circle class="dot" cx="52" cy="330" r="2"/><circle class="dot" cx="66" cy="330" r="2"/><circle class="dot" cx="80" cy="330" r="2"/><circle class="dot" cx="94" cy="330" r="2"/><circle class="dot" cx="108" cy="330" r="2"/><circle class="dot" cx="122" cy="330" r="2"/><circle class="dot" cx="136" cy="330" r="2"/><circle class="dot" cx="150" cy="330" r="2"/>
      <circle class="dot" cx="52" cy="344" r="2"/><circle class="dot" cx="66" cy="344" r="2"/><circle class="dot" cx="80" cy="344" r="2"/><circle class="dot" cx="94" cy="344" r="2"/><circle class="dot" cx="108" cy="344" r="2"/><circle class="dot" cx="122" cy="344" r="2"/><circle class="dot" cx="136" cy="344" r="2"/><circle class="dot" cx="150" cy="344" r="2"/>
    </g>
    <text class="compliance" font-size="19"><tspan x="37" y="432">Serving</tspan><tspan x="37" y="454">Homeowners</tspan><tspan x="37" y="476">in Florida with</tspan><tspan x="37" y="498">our main office in</tspan><tspan x="37" y="520">Miami-Dade.</tspan></text>
    <rect x="35" y="560" width="212" height="40" rx="20" fill="var(--brand-blue)" stroke="var(--white)" stroke-width="1.5"/>
    <text class="cta-label" x="141" y="585" font-size="14" text-anchor="middle">Contact us today for a consultation!</text>
    <path d="M37,652 l3,-1 2,4 -1,1 c1,2 2,3 4,4 l1,-1 4,2 -1,3 c-6,0 -12,-6 -12,-12z" fill="var(--white)"/>
    <text class="contact" x="52" y="663" font-size="12.5">1-800-555-0148</text>
    <path d="M38,676 l9,4 -4,1 3,4 -1,1 -3,-4 -1,4z" fill="var(--white)"/>
    <text class="contact" x="52" y="686" font-size="12.5">www.covenantshieldcounsel.example</text>
  </svg>
</div>
</body>
</html>
```